Psychologist needs a Sign & Postcard Design

I need the attached text & pictures to be arranged in a professional & impactful way so that people waiting to see other practitioners will notice my sign & walk away with the postcard (which matches the sign). Possibly the pictures of smiling people could be arranged on either side of the list called " Psychological Strategies for". The banner size is 830mm x 2000mm (Deskmart Retractable Exhibition Banner). The postcard size is DL 99 x 210mm (Printello). I'd like it set up so that the resolution works well for both individual print jobs. Also, I'd like the pictures to be sized well for each individual print job i.e. the format should be the same for both print jobs but if the scaled down version for the postcard means the pictures/text are too small then I would need it to be set up differently to make it readable & well presented. I like a collage style of picture arrangement. I'd rather the pictures weren't too large, but were still recognisable. I also have chosen a background colour which I think may be suitable. Please use the fonts I've used in the Info attachment. I would like the logo (my name & title etc) left as is. The final design should communicate a professional service & be positive.

```html
<!DOCTYPE html>
<html lang="en">
<head>
<meta charset="utf-8">
<title>Daniel McAlister – Clinical Psychologist</title>
<link href="https://fonts.googleapis.com/css2?family=Tinos:wght@400;700&family=Arimo:wght@400;700&display=swap" rel="stylesheet">
<style>
  :root {
    --paper: #f3f6fa;
    --navy: #1c2b55;
    --ink: #1e2433;
    --photo-warm: #c9a98c;
    --photo-blue: #8fa9c6;
    --photo-grey: #9d9d9b;
    --photo-green: #a9b58a;
  }
  html, body { margin: 0; padding: 0; overflow: hidden; }
  body { width: 1200px; height: 2888px; background: var(--paper); position: relative; font-family: "Arimo", Arial, sans-serif; color: var(--ink); }
  .photo { position: absolute; }
  .photo-strip-top .photo { top: 0; height: 320px; }
  .photo-strip-bottom .photo { top: 2528px; height: 360px; }
  .practitioner-name {
    position: absolute; top: 360px; left: 0; width: 1200px; margin: 0;
    text-align: center; font-family: "Tinos", "Times New Roman", serif; font-weight: 400;
    color: var(--navy); font-size: 168px; line-height: 172px; letter-spacing: 10px;
  }
  .practitioner-title {
    position: absolute; top: 768px; width: 1200px; text-align: center; margin: 0;
    font-size: 38px; letter-spacing: 10px; color: var(--navy); font-weight: 400;
  }
  .credentials {
    position: absolute; top: 842px; width: 1200px; text-align: center; margin: 0;
    font-size: 17px; line-height: 40px; font-weight: 700; letter-spacing: 4px; color: var(--navy);
  }
  .website { position: absolute; top: 956px; width: 1200px; text-align: center; font-size: 16px; font-weight: 700; color: var(--navy); letter-spacing: 1px; }
  .strategies-heading {
    position: absolute; top: 1052px; width: 1200px; text-align: center; margin: 0;
    font-size: 31px; font-weight: 700; letter-spacing: 3px; color: var(--navy);
  }
  .strategies-list {
    position: absolute; top: 1174px; width: 1200px; margin: 0; padding: 0; list-style: none;
    text-align: center; font-size: 30px; line-height: 36.3px; color: var(--ink);
  }
  .contact { position: absolute; top: 2250px; width: 1200px; text-align: center; color: var(--navy); }
  .contact-address { font-size: 20px; font-weight: 700; margin: 0; line-height: 30px; }
  .contact-phone { font-size: 20px; margin: 0; line-height: 30px; }
  .contact-hours { font-size: 17px; margin: 20px 0 0; }
</style>
</head>
<body>
  <div class="photo-strip-top">
    <div class="photo" style="left:0;width:488px;background:linear-gradient(135deg,#e7ebef,var(--photo-blue))" role="img" aria-label="Photo of a smiling man with glasses in a blue shirt"></div>
    <div class="photo" style="left:488px;width:272px;background:linear-gradient(160deg,#e2d7c8,var(--photo-warm))" role="img" aria-label="Photo of a smiling blonde woman"></div>
    <div class="photo" style="left:760px;width:440px;background:linear-gradient(160deg,#d6d6d4,var(--photo-grey))" role="img" aria-label="Black and white photo of a smiling older couple"></div>
  </div>

  <h1 class="practitioner-name">DANIEL<br>McALISTER</h1>
  <h2 class="practitioner-title">CLINICAL PSYCHOLOGIST</h2>
  <p class="credentials">MPsych., Member National Psychology Guild,<br>Member Guild of Clinical Practitioners</p>
  <div class="website">www.bayviewclinicpsych.com.au</div>

  <h3 class="strategies-heading">PSYCHOLOGICAL STRATEGIES FOR:</h3>
  <ul class="strategies-list">
    <li>Anxiety &amp; Worry</li>
    <li>Depression</li>
    <li>Sleep Difficulties</li>
    <li>Relationship Problems</li>
    <li>Panic</li>
    <li>Stress</li>
    <li>Burnout</li>
    <li>Overcoming Procrastination</li>
    <li>Achieving Life Goals</li>
    <li>Dealing with Difficult Personalities</li>
    <li>Anger</li>
    <li>Legal Concerns</li>
    <li>Obsessive Compulsive Behaviours</li>
    <li>Self Esteem Problems</li>
    <li>Trauma/Post Traumatic Stress</li>
    <li>Social Anxiety</li>
    <li>Confidence Building</li>
    <li>Phobias</li>
    <li>Assertiveness</li>
    <li>Body Image Issues</li>
    <li>Mood Problems</li>
    <li>Identity Difficulties</li>
    <li>Bipolar Disorder</li>
    <li>Post Natal Depression</li>
    <li>Grief &amp; Loss</li>
    <li>Coping with Life Change</li>
    <li>Overcoming Childhood Trauma</li>
    <li>Relaxation</li>
  </ul>

  <div class="contact">
    <p class="contact-address">Harbourside Health Hub, Ground Floor, 18 Wattle Crescent, Elmsford</p>
    <p class="contact-phone">Phone: 9555 0142</p>
    <p class="contact-hours">After Hours &amp; Saturday appointments available</p>
  </div>

  <div class="photo-strip-bottom">
    <div class="photo" style="left:0;width:408px;background:linear-gradient(150deg,#d9c2ae,#b0745a)" role="img" aria-label="Photo of a smiling red-haired woman"></div>
    <div class="photo" style="left:408px;width:312px;background:linear-gradient(160deg,#d8d8d6,var(--photo-grey))" role="img" aria-label="Black and white photo of a smiling teenage boy outdoors"></div>
    <div class="photo" style="left:720px;width:480px;background:linear-gradient(170deg,#dfe6d2,var(--photo-green))" role="img" aria-label="Photo of a smiling young woman relaxing on grass"></div>
  </div>
</body>
</html>
```